Letterhead for 3 attorney Workers' Comp law firm

We are a 3 attorney law office. We specialize in Workers' Compensation. Our office represents workers who are injured on the job, and the estates of workers who are killed one the job.
When we started our office, we created our own letterhead & have been using it for years. We've just recently hired the 3rd attorney, and were going to just add his name to the letterhead, but have decided we wanted to get a professionally designed letterhead and business cards at this point.
We want something that looks clean and professional. It must look good in black and white because we often make multiple copies of our documents. We're hoping for a design that resonates confidence, reliability and experience.
The design must include the firm name: Dorrance & Pike, PLLC. We would like the PLLC to be small compared to the Dorrance & Pike graphic. We also want to incorporate the attorney names: Ulric Dorrance, Janet Pike, and Lyle Hagberg. Our current letterhead has our contact info in the footer at the bottom of the page. We like that design, but are open to the idea of having it at the top. We'll leave that at the discretion of the designer. Our contact info is as follows: 472 S. Larchmont Avenue, Suite 315 Bellingham, WA 98117 Phone: 360-514-2967, Fax: 360-521-6079, and our website: www.dorrancepike-law.example
Target Market(s)
Clients, courts, other legal offices, doctors offices. These are the people who see our letterhead most frequently. It's not so much for marketing purposes, mainly so that we have a professional image when sending out documents.
Industry/Entity Type
Law Firm
Contact Information for Business Card
On the back of the business card: it can be designed, or be a template for filling in appointment reminder information (i.e. date, time, etc)
Colors
Designer to choose colors to be used in the design.
Requirements
Must have
- Must have our firm name at the top.
- Must include the attorney names.
- Must have all of our contact information (can be at top or bottom - whatever looks best with the design)
Nice to have
- A strong, confident design
Should not have
- We don't want the design to be playful, cartoony or busy.

```html
<!DOCTYPE html>
<html lang="en">
<head>
<meta charset="utf-8">
<title>Dorrance &amp; Pike, PLLC — Letterhead</title>
<link rel="stylesheet" href="https://fonts.googleapis.com/css2?family=Roboto+Slab:wght@300;400;700&display=swap">
<style>
  :root {
    --paper: #ffffff;
    --page-edge: #dcdcdc;
    --ink: #1e1e1e;
    --ink-soft: #5a5a5a;
    --band: #4a4a4a;
    --band-text: #ffffff;
    --rule: #b8b8b8;
  }
  * { margin: 0; padding: 0; box-sizing: border-box; }
  html, body {
    width: 934px;
    height: 1200px;
    overflow: hidden;
    background: var(--paper);
  }
  .letterhead {
    position: relative;
    width: 934px;
    height: 1200px;
    font-family: "Roboto Slab", Georgia, serif;
    color: var(--ink);
  }
  .page-edge {
    position: absolute;
    left: 14px; top: 14px;
    width: 906px; height: 1172px;
    border: 1px solid var(--page-edge);
  }
  .firm-block {
    position: absolute;
    left: 93px;
    top: 86px;
  }
  .firm-name {
    font-size: 35px;
    font-weight: 700;
    letter-spacing: -0.6px;
    line-height: 1;
    white-space: nowrap;
  }
  .firm-suffix {
    font-size: 27px;
    font-weight: 300;
    color: var(--ink-soft);
    letter-spacing: 0;
  }
  .attorney-band {
    display: inline-block;
    margin-top: 7px;
    padding: 2px 12px 2px 4px;
    background: var(--band);
    color: var(--band-text);
    font-size: 13.5px;
    font-weight: 300;
    letter-spacing: -0.2px;
    line-height: 16px;
    white-space: nowrap;
    clip-path: polygon(0 0, 100% 0, calc(100% - 4px) 100%, 0 100%);
  }
  .contact-block {
    position: absolute;
    left: 679px;
    top: 108px;
    font-size: 12.5px;
    font-weight: 300;
    line-height: 16px;
    letter-spacing: -0.1px;
  }
  .contact-block p { margin-bottom: 7px; }
  .contact-label { font-weight: 700; }
  .footer-rule {
    position: absolute;
    left: 92px;
    top: 1106px;
    width: 748px;
    height: 0;
    border-top: 1.5px solid var(--rule);
  }
</style>
</head>
<body>
  <main class="letterhead">
    <div class="page-edge"></div>

    <header class="firm-block">
      <h1 class="firm-name">Dorrance &amp; Pike, <span class="firm-suffix">PLLC</span></h1>
      <div class="attorney-band">Attorney: Ulric Dorrance, Janet Pike, and Lyle Hagberg</div>
    </header>

    <address class="contact-block" style="font-style:normal">
      <p><span class="contact-label">w.</span> www.dorrancepike-law.example</p>
      <p>472 S. Larchmont Avenue,<br>Suite 315 Bellingham,<br>WA 98117</p>
      <p><span class="contact-label">t.</span> 360-514-2967<br><span class="contact-label">f.</span> 360-521-6079</p>
    </address>

    <div class="footer-rule"></div>
  </main>
</body>
</html>
```